Typing Service Business Card Design

Need a new business card design for new logo update. The Ledger Scribes is an outsourced typing service. We type audio / voice files into word documents. We are a professional service that is recognised in the industry over the past 15 years and have a strong connection to our brand. The final design should be professional, simple, yet effective.

Corinna Waldrop
Director

corinna@lsx.com.au
www.theledgerscribes.com.au

```html
<!DOCTYPE html>
<html lang="en">
<head>
<meta charset="utf-8">
<title>The Ledger Scribes – Business Card</title>
<link rel="stylesheet" href="https://fonts.googleapis.com/css2?family=Arimo:wght@400;700&family=Roboto+Condensed:wght@400;700&display=swap">
<style>
  :root {
    --backdrop: #e6e4e2;
    --card: #1c1c1e;
    --card-edge: #2a2a2c;
    --magenta: #d6409f;
    --ink-light: #f2f2f2;
    --ink-muted: #b9b9bb;
    --divider: #8a8a8c;
  }
  * { margin: 0; padding: 0; box-sizing: border-box; }
  html, body {
    width: 1200px; height: 787px; overflow: hidden;
    background: var(--backdrop);
  }
  .sheet {
    position: relative; width: 1200px; height: 787px;
    display: flex; align-items: center; justify-content: center; gap: 50px;
  }
  .card {
    position: relative; width: 520px; height: 297px;
    background: var(--card);
    border: 1px solid var(--card-edge);
    box-shadow: 0 10px 28px rgba(0,0,0,0.22);
  }

  /* Back of card */
  .card-back .brand-mark {
    position: absolute; left: 0; right: 0; top: 96px;
    display: flex; align-items: center; justify-content: center; gap: 14px;
  }
  .brand-square {
    width: 22px; height: 22px; border: 3px solid var(--magenta);
  }
  .brand-name {
    font-family: "Roboto Condensed", sans-serif; font-weight: 700;
    color: var(--magenta); white-space: nowrap;
  }
  .card-back .brand-name { font-size: 36px; letter-spacing: 0.5px; }
  .card-back .site-url {
    position: absolute; left: 30px; bottom: 30px;
    font-family: "Arimo", sans-serif; font-size: 13px;
    letter-spacing: 2.4px; color: var(--ink-muted);
  }

  /* Front of card */
  .card-front .logo-block {
    position: absolute; left: 26px; top: 116px; width: 214px;
  }
  .card-front .brand-name { font-size: 24px; line-height: 1; }
  .tagline {
    margin-top: 8px;
    font-family: "Roboto Condensed", sans-serif; font-size: 15px;
    color: var(--ink-light); white-space: nowrap;
  }
  .divider {
    position: absolute; left: 258px; top: 70px; width: 1px; height: 150px;
    background: linear-gradient(to bottom, transparent, var(--divider) 30%, var(--divider) 70%, transparent);
  }
  .contact {
    position: absolute; left: 278px; top: 104px;
    font-family: "Arimo", sans-serif; color: var(--ink-light);
  }
  .person-name {
    font-size: 22px; font-weight: 700; color: var(--magenta); letter-spacing: 0.3px;
    white-space: nowrap;
  }
  .person-role { font-size: 14px; margin-top: 2px; }
  .contact-list { list-style: none; margin-top: 18px; }
  .contact-list li {
    display: flex; align-items: center; gap: 8px;
    font-size: 14px; margin-bottom: 7px; white-space: nowrap;
  }
  .contact-icon { width: 14px; height: 14px; flex: none; }
</style>
</head>
<body>
<main class="sheet">
  <section class="card card-back" aria-label="Card back">
    <div class="brand-mark">
      <span class="brand-square" aria-hidden="true"></span>
      <span class="brand-name">The Ledger Scribes</span>
    </div>
    <p class="site-url">www.theledgerscribes.com.au</p>
  </section>

  <section class="card card-front" aria-label="Card front">
    <div class="logo-block">
      <p class="brand-name">The Ledger Scribes</p>
      <p class="tagline">Spoken in. Typed out.</p>
    </div>
    <div class="divider" aria-hidden="true"></div>
    <div class="contact">
      <p class="person-name">Corinna Waldrop</p>
      <p class="person-role">Director</p>
      <ul class="contact-list">
        <li>
          <svg class="contact-icon" viewBox="0 0 14 14" aria-hidden="true">
            <rect x="0.5" y="2.5" width="13" height="9" fill="var(--magenta)"/>
            <path d="M0.5 2.5 L7 8 L13.5 2.5" fill="none" stroke="var(--card)" stroke-width="1.2"/>
          </svg>
          corinna@lsx.com.au
        </li>
        <li>
          <svg class="contact-icon" viewBox="0 0 14 14" aria-hidden="true">
            <circle cx="7" cy="7" r="6.5" fill="var(--magenta)"/>
            <path d="M0.8 7 H13.2 M7 0.8 C4 4 4 10 7 13.2 M7 0.8 C10 4 10 10 7 13.2" fill="none" stroke="var(--card)" stroke-width="1"/>
          </svg>
          theledgerscribes.com.au
        </li>
      </ul>
    </div>
  </section>
</main>
</body>
</html>
```